Vantrel Web Services

This is a new It services company operating in Perth western Australia

we need a website that is easy to navigate without a cluttered feel to it it should have the following links and pages

About Us
Services
Clients
Contact Us
MY Vantrel (login for clients)

Hi it is a web based IT services company so we would expect customers to come to the website for 2 different purposes the first is to enquire about our services and then as they become customers come to our website to manage their services so whilst they are seperate we want do not want it to look like 2 different websites

hope this helps

Hi to update this we need a home page and templates for sub pages

this is a design brief only and not the coding of the pages or building of the site

```html
<!DOCTYPE html>
<html lang="en">
<head>
<meta charset="utf-8">
<title>Vantrel Web Services</title>
<link href="https://fonts.googleapis.com/css2?family=Open+Sans:wght@300;400;600;700&family=Raleway:wght@400;500;600;700&display=swap" rel="stylesheet">
<style>
:root{
  --navy:#0a2a8a;
  --blue-1:#00309a;
  --blue-2:#1f4fb3;
  --blue-3:#4a6fc0;
  --red:#c4161c;
  --red-dark:#8b0b0b;
  --red-bar:#9a0a0a;
  --ink:#555c66;
  --muted:#7a828c;
  --footer:#2f383d;
  --footer-text:#aab2b8;
  --light:#f4f4f4;
  --line:#d6d9dc;
  --white:#ffffff;
}
*{box-sizing:border-box;margin:0;padding:0}
html,body{width:965px;height:1200px;overflow:hidden}
body{position:relative;background:#fafbfb;font-family:"Raleway",sans-serif;color:var(--ink)}
.abs{position:absolute}

.topbar{left:0;top:0;width:965px;height:28px;background:var(--light);border-bottom:1px solid #e2e2e2}
.topbar-item{top:8px;font-size:8.5px;color:#333;display:flex;align-items:center;gap:5px}

.header{left:0;top:28px;width:965px;height:68px;background:var(--white)}
.brand{left:132px;top:8px;display:flex;align-items:center;gap:8px}
.brand-dot{width:50px;height:50px;border-radius:50%;background:var(--red)}
.brand-name{font-family:"Open Sans",sans-serif;font-weight:700;font-size:27px;letter-spacing:2px;color:var(--navy)}
.nav{top:30px;font-size:10.5px;font-weight:600;color:#6a7480}
.nav.is-active{color:var(--navy);font-weight:700}

.hero{left:0;top:96px;width:965px;height:378px;
  background:radial-gradient(circle at 37% 35%,#ffd0d6 0%,#e07a86 14%,#a14a57 32%,#5a2a33 55%,#2a1a20 80%),linear-gradient(90deg,#6a3a45,#201418)}
.hero-caption{left:520px;top:221px;width:325px;height:133px;background:rgba(0,0,0,.82);padding:30px 32px}
.hero-sub{font-family:"Open Sans",sans-serif;font-weight:400;font-size:22px;color:var(--white);line-height:1}
.hero-title{font-family:"Open Sans",sans-serif;font-weight:700;font-size:34px;color:var(--white);line-height:1.1;margin-top:6px}
.hero-arrow{top:262px;width:42px;height:45px;background:#0d2f8a;display:flex;align-items:center;justify-content:center}

.panel{top:474px;width:241px;height:224px;padding:26px 32px;color:var(--white)}
.panel h2{font-family:"Open Sans",sans-serif;font-weight:700;font-size:17px}
.panel h3{font-size:9.5px;font-weight:700;margin-top:14px;letter-spacing:.2px}
.panel p{font-size:9px;line-height:13.6px;margin-top:8px}
.panel ul{list-style:none;margin-top:6px}
.panel li{font-size:9px;line-height:19px;display:flex;align-items:center;gap:5px}
.panel li::before{content:"";border-left:4px solid var(--white);border-top:3px solid transparent;border-bottom:3px solid transparent}
.pill{position:absolute;left:32px;top:177px;height:24px;padding:0 9px;border-radius:12px;background:#eef0f2;border:1px solid #cfd3d8;color:#666;font-size:8px;display:flex;align-items:center}
.field{width:184px;height:30px;background:var(--white);margin-top:8px;display:flex;align-items:center;justify-content:space-between;padding:0 10px;font-size:9px;color:#9aa0a6}

.section-title{font-family:"Open Sans",sans-serif;font-weight:400;font-size:18px;color:var(--navy)}
.avatar{left:134px;top:766px;width:60px;height:60px;border-radius:50%;background:radial-gradient(circle at 50% 45%,#c89c86,#7a4c3c)}
.person-name{left:124px;top:842px;width:80px;text-align:center;font-size:11.5px;font-weight:600;color:#666}
.person-role{left:114px;top:859px;width:100px;text-align:center;font-size:9px;color:#777}
.quote{left:223px;top:764px;width:369px;height:106px;border:1px solid var(--line);background:#f3f4f5;padding:14px 22px;font-style:italic;font-size:11.5px;line-height:18px;color:#7a8088}
.quote::before{content:"";position:absolute;left:-8px;top:28px;width:14px;height:14px;background:#f3f4f5;border-left:1px solid var(--line);border-bottom:1px solid var(--line);transform:rotate(45deg)}
.news-thumb{left:613px;width:41px;height:42px;background:linear-gradient(135deg,#8a98a8,#3c4650)}
.news-text{left:664px;width:180px;font-size:9px;line-height:15px;color:#7a828c}
.news-date{color:#555}

.clients{left:0;top:902px;width:965px;height:84px;background:radial-gradient(ellipse at 45% 70%,#c55050 0%,#a11b1b 40%,var(--red-dark) 80%)}
.clients-title{left:129px;top:936px;font-family:"Open Sans",sans-serif;font-size:17px;color:var(--white)}
.client-name{top:934px;font-family:"Raleway",sans-serif;font-weight:700;font-size:17px;color:var(--white)}

.footer{left:0;top:986px;width:965px;height:176px;background:var(--footer)}
.footer-brand{left:120px;top:1018px;display:flex;align-items:center;gap:6px}
.footer-brand .brand-dot{width:34px;height:34px;background:var(--white)}
.footer-brand .brand-name{color:var(--white);font-size:19px}
.footer-about{left:125px;top:1075px;width:170px;font-size:9px;line-height:15.2px;color:var(--footer-text)}
.footer-head{top:1016px;font-size:9.5px;font-weight:500;color:var(--white)}
.footer-link{left:373px;font-size:9px;color:var(--footer-text);display:flex;align-items:center;gap:8px}
.footer-link::before{content:"";border-left:3px solid #8a9298;border-top:3px solid transparent;border-bottom:3px solid transparent}
.social{top:1044px;width:24px;height:24px;background:var(--white)}
.contact-row{left:676px;font-size:9px;line-height:15px;color:var(--footer-text);display:flex;gap:11px}
.contact-row svg{flex:none;margin-top:1px}

.bottombar{left:0;top:1162px;width:965px;height:38px;background:var(--red-bar)}
.bottom-text{top:1176px;font-size:9px;font-weight:600;color:var(--white)}
</style>
</head>
<body>

<div class="abs topbar"></div>
<div class="abs topbar-item" style="left:636px">
  <svg width="23" height="11" viewBox="0 0 23 11"><path d="M0 2h5M1 5h4M2 8h3" stroke="#c4161c" stroke-width="1"/><rect x="7" y=".5" width="15" height="10" fill="none" stroke="#c4161c"/><path d="M7 .5l7.5 6 7.5-6" fill="none" stroke="#c4161c"/></svg>
  info@vantrel.com
</div>
<div class="abs topbar-item" style="left:754px">
  <svg width="12" height="12" viewBox="0 0 12 12"><path d="M3 1l2 2.5-1.2 1.5c.6 1.3 1.6 2.4 3 3l1.5-1.2L11 8.5 9.8 11C5 10.5 1.5 7 1 2.2z" fill="#c4161c"/></svg>
  +61 8 9412 7730
</div>

<header class="abs header">
  <div class="abs brand"><span class="brand-dot"></span><span class="brand-name">VANTREL</span></div>
  <span class="abs nav is-active" style="left:532px">Home</span>
  <span class="abs nav" style="left:592px">About Us</span>
  <span class="abs nav" style="left:665px">Services</span>
  <span class="abs nav" style="left:738px">Clients</span>
  <span class="abs nav" style="left:799px">Contact</span>
</header>

<section class="abs hero" role="img" aria-label="Photo of a businessman touching glowing hexagon shapes on a virtual screen"></section>
<div class="abs hero-caption">
  <div class="hero-sub">Trusted in Perth, Australia</div>
  <div class="hero-title">IT SOLUTIONS</div>
</div>
<div class="abs hero-arrow" style="left:0"><svg width="10" height="14" viewBox="0 0 10 14"><path d="M8 1L2 7l6 6" fill="none" stroke="#fff" stroke-width="2"/></svg></div>
<div class="abs hero-arrow" style="left:921px;width:44px"><svg width="10" height="14" viewBox="0 0 10 14"><path d="M2 1l6 6-6 6" fill="none" stroke="#fff" stroke-width="2"/></svg></div>

<section class="abs panel" style="left:122px;background:var(--blue-1)">
  <h2>About Us</h2>
  <h3>BRINGING THE BEST IT SERVICES</h3>
  <p>Lorem ipsum dolor sit amet, consectetur adipisicing elitsed do eiusmod tempor incididunt ut labore et, sed do eiusmod tempor incididunt ut labore et dolore magna aliqua.</p>
  <span class="pill">Read More</span>
</section>
<section class="abs panel" style="left:363px;background:var(--blue-2)">
  <h2>Our Services</h2>
  <h3>OUR SERVICES INCLUDE::</h3>
  <ul>
    <li>IT Consultation</li>
    <li>Systems Management</li>
    <li>Network Engineering</li>
    <li>More..</li>
  </ul>
  <span class="pill">Read More</span>
</section>
<section class="abs panel" style="left:604px;background:var(--blue-3)">
  <h2>MY Vantrel</h2>
  <h3>CLIENT LOGIN</h3>
  <div class="field">Name
    <svg width="9" height="12" viewBox="0 0 9 12"><circle cx="4.5" cy="3" r="2.6" fill="#b5b9be"/><path d="M0 12c0-4 1.8-5.5 4.5-5.5S9 8 9 12z" fill="#b5b9be"/></svg></div>
  <div class="field">Password
    <svg width="11" height="12" viewBox="0 0 11 12"><path d="M3 5V3.5a2.5 2.5 0 015 0V5" fill="none" stroke="#b5b9be" stroke-width="1.5"/><rect x="0" y="5" width="11" height="7" rx="1" fill="#b5b9be"/></svg></div>
  <span class="pill" style="padding:0 18px">Login</span>
</section>

<h2 class="abs section-title" style="left:129px;top:728px">Client Testimonial</h2>
<div class="abs avatar" role="img" aria-label="Portrait photo of the managing director"></div>
<div class="abs person-name">Mara Linden</div>
<div class="abs person-role">Managing Director</div>
<blockquote class="abs quote">“Vestibulum blandit faucibus urna in hendrerit. Vivamus leo dui, bibendum vitae hendrerit ac, volutpat quis dolor. Maece-nas id lacinia odio, et malesuada lectus. Nulla et ante non metus consectetur vestibulum sed quis dolor.”</blockquote>

<h2 class="abs section-title" style="left:611px;top:728px">Recent News</h2>
<div class="abs news-thumb" style="top:766px" role="img" aria-label="Photo of colleagues talking in an office"></div>
<div class="abs news-text" style="top:763px">Fusce gravida tortor felis, ac dictum risus sagittiso eiusmod tempor incididunt ut<br><span class="news-date">October 15, 2013</span></div>
<div class="abs news-thumb" style="top:826px" role="img" aria-label="Photo of hands using a tablet"></div>
<div class="abs news-text" style="top:822px">Fusce gravida tortor felis, ac dictum risus sagittiso eiusmod tempor incididunt ut<br><span class="news-date">October 15, 2013</span></div>

<section class="abs clients"></section>
<h2 class="abs clients-title">Our Clients</h2>
<span class="abs client-name" style="left:274px">Halvory</span>
<span class="abs client-name" style="left:388px">Brightwell</span>
<span class="abs client-name" style="left:520px">Osterline</span>
<span class="abs client-name" style="left:652px">Kivamo</span>
<span class="abs client-name" style="left:768px">Pelling</span>

<footer class="abs footer"></footer>
<div class="abs footer-brand"><span class="brand-dot"></span><span class="brand-name">VANTREL</span></div>
<p class="abs footer-about">Donec volutpat, mi vel egestas eleif-end, dolor arcu iaculis nunc. Fusce gravida tortor felis, ac dictum risus</p>

<h4 class="abs footer-head" style="left:372px">Navigation</h4>
<span class="abs footer-link" style="top:1049px">Home</span>
<span class="abs footer-link" style="top:1072px">About Vantrel</span>
<span class="abs footer-link" style="top:1094px">Our Services</span>
<span class="abs footer-link" style="top:1117px">Clients</span>

<h4 class="abs footer-head" style="left:494px">Social</h4>
<span class="abs social" style="left:497px" aria-label="Social link 1"></span>
<span class="abs social" style="left:533px" aria-label="Social link 2"></span>
<span class="abs social" style="left:569px" aria-label="Social link 3"></span>
<span class="abs social" style="left:605px" aria-label="News feed"></span>

<h4 class="abs footer-head" style="left:674px">Contact Details</h4>
<div class="abs contact-row" style="top:1047px">
  <svg width="12" height="12" viewBox="0 0 12 12"><path d="M3 1l2 2.5-1.2 1.5c.6 1.3 1.6 2.4 3 3l1.5-1.2L11 8.5 9.8 11C5 10.5 1.5 7 1 2.2z" fill="#8a9298"/></svg>
  +61 8 9000 1234</div>
<div class="abs contact-row" style="top:1070px">
  <svg width="12" height="10" viewBox="0 0 12 10"><rect x=".5" y=".5" width="11" height="9" fill="none" stroke="#8a9298"/><path d="M.5 .5l5.5 5 5.5-5" fill="none" stroke="#8a9298"/></svg>
  hello@vantrel.com</div>
<div class="abs contact-row" style="top:1093px">
  <svg width="12" height="14" viewBox="0 0 12 14"><path d="M6 0a5 5 0 015 5c0 4-5 9-5 9S1 9 1 5a5 5 0 015-5z" fill="#8a9298"/><circle cx="6" cy="5" r="2" fill="#2f383d"/></svg>
  <span>Your Address, Your Country<br>Your Zip Code</span></div>

<div class="abs bottombar"></div>
<span class="abs bottom-text" style="left:125px">Copyright © 2014 - Vantrel. All Rights reserved</span>
<span class="abs bottom-text" style="left:732px">Privacy Policy</span>
<span class="abs bottom-text" style="left:826px">Sitemap</span>

</body>
</html>
```